Business Card Design

We need a business card design for a new company based in Allen, Texas. (outside of Dallas,Texas) We offer Business Management Solutions to Entrepreneurs, as well as Corporate Businesses. Our product line offers solutions to Image, Branding, Social Media marketing, business development strategies, banking / funding solutions, just to name a few. We would like to see designs that convey strength and confidence. I have attached a sample design of our company name. Designers you may use company name as either: Vorlix or Vorlix Corporation, depending on the design layout.

Please show alternate color of Black as well.

Industry/Entity Type

Business

Contact Information for Business Card

Vorlix Corporation

2847 E. Hollowbrook Drive, STE 410
Larkmoor, CO 80214
Office: 469.318.7742
Fax: 469.318.7743

Dr. Miles Dunworth
Business Development Director

```html
<!DOCTYPE html>
<html lang="en">
<head>
<meta charset="utf-8">
<title>Vorlix Corporation – Business Card</title>
<link href="https://fonts.googleapis.com/css2?family=Questrial&family=Mulish:wght@400;700&display=swap" rel="stylesheet">
<style>
  :root {
    --stage: #e7e5e2;
    --card-black: #111111;
    --card-black-edge: #262626;
    --silver: #c4c4c4;
    --ink: #111111;
    --muted: #8a8a8a;
    --paper: #ffffff;
    --globe-light: #f3f3f3;
    --globe-dark: #d2d2d2;
  }
  * { margin: 0; padding: 0; box-sizing: border-box; }
  html, body { width: 1200px; height: 784px; overflow: hidden; }
  body {
    background: var(--stage);
    position: relative;
    font-family: "Mulish", sans-serif;
  }
  .card {
    position: absolute;
    top: 237px;
    width: 540px;
    height: 309px;
    overflow: hidden;
    box-shadow: 0 6px 18px rgba(0,0,0,0.18);
  }
  .card--front {
    left: 40px;
    background: radial-gradient(ellipse at 50% 40%, var(--card-black-edge) 0%, var(--card-black) 70%);
    display: flex;
    align-items: center;
    justify-content: center;
  }
  .front-logo {
    font-family: "Questrial", sans-serif;
    font-size: 118px;
    color: var(--silver);
    letter-spacing: -2px;
    line-height: 1;
    margin-top: -20px;
  }
  .card--back {
    left: 620px;
    background: var(--paper);
  }
  .back-logo {
    position: absolute;
    left: 30px;
    top: 38px;
    font-family: "Questrial", sans-serif;
    font-size: 84px;
    color: var(--ink);
    letter-spacing: -1px;
    line-height: 1;
  }
  .globe-art {
    position: absolute;
    right: 14px;
    top: 44px;
    width: 150px;
    height: 150px;
    border-radius: 50%;
    background: radial-gradient(circle at 35% 35%, var(--globe-light) 0%, var(--globe-dark) 100%);
    opacity: 0.8;
  }
  .holder {
    position: absolute;
    left: 34px;
    top: 156px;
  }
  .holder-name {
    font-size: 17px;
    font-weight: 700;
    color: var(--ink);
    line-height: 1.1;
  }
  .holder-title {
    font-size: 11.5px;
    color: var(--muted);
    margin-top: 2px;
  }
  .contact-list {
    position: absolute;
    left: 30px;
    top: 198px;
    list-style: none;
    font-size: 14px;
    color: var(--ink);
    line-height: 17px;
  }
  .contact-item {
    display: flex;
    align-items: flex-start;
    gap: 6px;
  }
  .contact-icon {
    width: 14px;
    height: 14px;
    margin-top: 2px;
    flex: none;
    fill: var(--muted);
  }
  .band {
    position: absolute;
    left: 0;
    right: 0;
    top: 278px;
    height: 20px;
    background: var(--card-black);
  }
</style>
</head>
<body>
  <section class="card card--front" aria-label="Card front">
    <div class="front-logo">vorlix</div>
  </section>

  <section class="card card--back" aria-label="Card back">
    <div class="back-logo">vorlix</div>
    <div class="globe-art" role="img" aria-label="Faint grey wireframe globe decoration"></div>

    <div class="holder">
      <p class="holder-name">Dr. Miles Dunworth</p>
      <p class="holder-title">Business Development Director</p>
    </div>

    <ul class="contact-list">
      <li class="contact-item">
        <svg class="contact-icon" viewBox="0 0 16 16" aria-label="Office"><path d="M3.5 1.5l2.5 0 1 3.5-1.7 1.2c.8 1.8 2.2 3.2 4 4l1.2-1.7 3.5 1v2.5c0 .8-.7 1.5-1.5 1.5C6.9 13.5 2 8.6 2 3c0-.8.7-1.5 1.5-1.5z"/></svg>
        <span>469.318.7742</span>
      </li>
      <li class="contact-item">
        <svg class="contact-icon" viewBox="0 0 16 16" aria-label="Fax"><rect x="4" y="1.5" width="8" height="4.5"/><rect x="1.5" y="6.5" width="13" height="6" rx="1"/><rect x="4" y="10.5" width="8" height="4" fill="#fff" stroke="#8a8a8a"/></svg>
        <span>469.318.7743</span>
      </li>
      <li class="contact-item">
        <svg class="contact-icon" viewBox="0 0 16 16" aria-label="Address"><path d="M8 1.5l7 6h-2v7H9.8v-4.5H6.2v4.5H3v-7H1z"/></svg>
        <span>2847 E. Hollowbrook Drive,<br>STE 410 Larkmoor, CO 80214</span>
      </li>
    </ul>

    <div class="band"></div>
  </section>
</body>
</html>
```